Aquaponic greenhouse needs a business brochure that shows what a unique system we have

We would like to expand our marketing beyond social media. We are a aquaponic greenhouse where we use fish to fertilize the water so that we don't have to use any chemicals in the system. This method is sustainable and environmentally friendly. We grow in a climate controlled system year round and deliver the freshest produce directly to our local families, schools and restaurants. All of our produce is grown from seed, closely monitored during the growing cycle, hand picked and hand packaged for our customers.

Aquaponics - The combination of Aquaculture (raising fish) and Hydroponics (growing plants in a soilless system)

Sustainable - Closed loop system using the same water for the fish and plants.

Local - Delaware natives providing healthy eating opportunities for our neighbors throughout the state.

Chemical and Soil Free

Largest in the First State - With over 15,000 square feet of a climate controlled environment, we can grow the freshest produce year round with consistent output.

Target Market(s)

Customers and those who don’t use social media

Industry/Entity Type

Agribusiness

Font styles to use
Sans Serif

Colors
0255a3
32b8a4
9bcb3c
cadf82

Requirements
Must have
• Our logo (attached) some personalized pictures (can be found on our website www.bluefernharvest.com) and areas where we can customize our written content. Must have editable text and be able to replace pictures as we grow.
Nice to have
• Options for a tri-fold and bi-fold brochures

```html
<!DOCTYPE html>
<html lang="en">
<head>
<meta charset="utf-8">
<title>Blue Fern Harvest – Flyer</title>
<link href="https://fonts.googleapis.com/css2?family=Montserrat:ital,wght@0,400;0,600;0,700;1,400&family=Oswald:wght@500;600&display=swap" rel="stylesheet">
<style>
  :root{
    --brand-blue:#0255a3;
    --sky-blue:#1c8fd8;
    --teal:#32b8a4;
    --leaf-green:#9bcb3c;
    --pale-green:#cadf82;
    --deep-green:#5fa82a;
    --gold:#e3b866;
    --gold-light:#f6dca0;
    --ink:#1d1d1d;
    --body-grey:#6b6b6b;
    --page-bg:#e7e8ea;
    --paper:#ffffff;
  }
  *{box-sizing:border-box;margin:0;padding:0}
  html,body{width:1200px;height:840px;overflow:hidden;background:var(--page-bg)}
  body{font-family:"Montserrat",Arial,sans-serif;position:relative}

  .flyer{
    position:absolute;left:317px;top:20px;width:566px;height:800px;
    background:var(--paper);overflow:hidden;
    box-shadow:0 6px 24px rgba(0,0,0,.12);
  }
  .flyer__waves{position:absolute;inset:0;width:566px;height:800px}

  .brand{position:absolute;left:40px;top:44px;display:flex;align-items:center;gap:10px}
  .brand__dot{width:30px;height:30px;border-radius:50%;background:var(--teal)}
  .brand__name{font-family:"Montserrat",sans-serif;font-weight:700;font-size:19px;color:var(--brand-blue);letter-spacing:.3px}

  .intro{
    position:absolute;left:40px;top:118px;width:250px;
    font-size:10.5px;line-height:1.35;color:var(--ink);text-align:justify;
  }

  .photo{position:absolute}
  .photo--lettuce{
    right:0;top:20px;width:260px;height:250px;
    background:radial-gradient(closest-side at 55% 50%,#4e8f1f 0%,#7fc23a 45%,#a6d862 75%,rgba(255,255,255,0) 100%);
  }
  .photo--grower{
    right:0;top:500px;width:290px;height:300px;
    background:radial-gradient(closest-side at 55% 50%,#2b59c8 0%,#3f6fd6 45%,rgba(90,130,220,.55) 75%,rgba(255,255,255,0) 100%);
  }
  .photo--greens{
    left:170px;top:690px;width:300px;height:110px;
    background:radial-gradient(closest-side at 50% 55%,#6fb52e 0%,#a3d665 60%,rgba(255,255,255,0) 100%);
  }

  .preorder{position:absolute;left:40px;top:292px;color:#fff}
  .preorder__title{font-weight:600;font-size:18px;line-height:1.1;text-transform:uppercase;margin-bottom:10px}
  .preorder__list{list-style:none}
  .preorder__item{font-size:11px;font-style:italic;line-height:1.55;display:flex;align-items:center;gap:7px}
  .preorder__tick{width:12px;height:10px;flex:none}

  .delivery{
    position:absolute;left:300px;top:268px;width:250px;
    font-family:"Oswald",sans-serif;font-weight:500;font-size:23px;line-height:1.18;
    color:#fff;text-transform:uppercase;text-align:center;letter-spacing:.5px;
  }

  .offer-badge{
    position:absolute;left:296px;top:382px;width:124px;height:124px;border-radius:50%;
    background:radial-gradient(circle at 40% 35%,var(--gold-light),var(--gold) 70%);
    display:flex;flex-direction:column;align-items:center;justify-content:center;
    font-family:"Oswald",sans-serif;color:#111;line-height:1;
  }
  .offer-badge__amount{font-size:44px;font-weight:600}
  .offer-badge__note{font-size:19px;font-weight:600;margin-top:2px}

  .about{position:absolute;left:36px;top:522px;width:270px}
  .about__title{font-weight:700;font-size:16px;color:var(--ink);text-transform:uppercase;margin-bottom:10px}
  .about__text{font-size:11.5px;line-height:1.45;color:var(--body-grey);text-align:justify}

  .contact{position:absolute;left:26px;top:628px}
  .contact__phone{
    display:inline-block;background:var(--deep-green);color:#fff;
    font-family:"Oswald",sans-serif;font-weight:500;font-size:19px;
    padding:3px 16px;border-radius:4px;transform:skewX(-8deg);
  }
  .contact__web{
    display:block;margin-top:4px;color:var(--deep-green);
    font-family:"Oswald",sans-serif;font-weight:500;font-size:19px;transform:skewX(-8deg);
  }
</style>
</head>
<body>
  <main class="flyer">
    <svg class="flyer__waves" viewBox="0 0 566 800" aria-hidden="true">
      <defs>
        <linearGradient id="greenBand" x1="0" y1="0" x2="1" y2="1">
          <stop offset="0" stop-color="#7cbf2e"/>
          <stop offset="1" stop-color="#b4dc52"/>
        </linearGradient>
        <linearGradient id="blueBand" x1="0" y1="0" x2="1" y2="1">
          <stop offset="0" stop-color="#1d9be0"/>
          <stop offset="1" stop-color="#0255a3"/>
        </linearGradient>
      </defs>
      <path d="M0,288 C120,262 250,258 566,246 L566,470 C400,510 250,505 0,488 Z" fill="url(#greenBand)"/>
      <path d="M262,262 C380,246 470,238 566,232 L566,570 C490,500 420,472 340,472 Z" fill="url(#blueBand)"/>
      <path d="M0,488 C140,502 260,488 340,476 C430,464 500,480 566,520 L566,800 L0,800 Z" fill="#ffffff"/>
    </svg>

    <div class="photo photo--lettuce" role="img" aria-label="Photo of a fresh head of green leaf lettuce"></div>

    <div class="brand">
      <span class="brand__dot"></span>
      <span class="brand__name">Blue Fern Harvest</span>
    </div>

    <p class="intro">We are the largest commercial Aquaponics greenhouse in Delaware! With over 15,000 square feet of space, we offer lettuces, greens and fish year-round directly to consumers and to local schools and restaurants. Check out our products page to see what is currently available for pickup throughout the First State.</p>

    <section class="preorder">
      <h2 class="preorder__title">Pre-order for<br>pick up</h2>
      <ul class="preorder__list">
        <li class="preorder__item"><svg class="preorder__tick" viewBox="0 0 12 10"><path d="M1 5 L4.5 8.5 L11 1.5" fill="none" stroke="#fff" stroke-width="2"/></svg>Wildfire Lettuce Mix</li>
        <li class="preorder__item"><svg class="preorder__tick" viewBox="0 0 12 10"><path d="M1 5 L4.5 8.5 L11 1.5" fill="none" stroke="#fff" stroke-width="2"/></svg>Summer Crisp Lettuce</li>
        <li class="preorder__item"><svg class="preorder__tick" viewBox="0 0 12 10"><path d="M1 5 L4.5 8.5 L11 1.5" fill="none" stroke="#fff" stroke-width="2"/></svg>Romaine Lettuce</li>
        <li class="preorder__item"><svg class="preorder__tick" viewBox="0 0 12 10"><path d="M1 5 L4.5 8.5 L11 1.5" fill="none" stroke="#fff" stroke-width="2"/></svg>Waldmann's Lettuce</li>
        <li class="preorder__item"><svg class="preorder__tick" viewBox="0 0 12 10"><path d="M1 5 L4.5 8.5 L11 1.5" fill="none" stroke="#fff" stroke-width="2"/></svg>Raw Honey 16 oz.</li>
        <li class="preorder__item"><svg class="preorder__tick" viewBox="0 0 12 10"><path d="M1 5 L4.5 8.5 L11 1.5" fill="none" stroke="#fff" stroke-width="2"/></svg>Swiss Chard</li>
      </ul>
    </section>

    <h2 class="delivery">We are now offering<br>personalized<br>delivery on orders</h2>

    <div class="photo photo--grower" role="img" aria-label="Photo of the grower in a blue shirt holding a tray of fresh lettuce"></div>
    <div class="photo photo--greens" role="img" aria-label="Photo of a tray of leafy greens"></div>

    <div class="offer-badge">
      <span class="offer-badge__amount">$100</span>
      <span class="offer-badge__note">OR MORE.</span>
    </div>

    <section class="about">
      <h3 class="about__title">Little about us:</h3>
      <p class="about__text">The largest aquaponics greenhouse in the 1st state offering locally grown, sustainable, soil-less produce year round.</p>
    </section>

    <div class="contact">
      <span class="contact__phone">Call us: +1 302-555-0148</span>
      <span class="contact__web">www.bluefernharvest.com</span>
    </div>
  </main>
</body>
</html>
```